RTV CRAFTED

building services
decks
pergola
renovation
extensions
general building

Target Market(s)

middle to upper class

Industry/Entity Type

building

Contact Information for Business Card

my details 0427839152 pkharlow47@mailvane.net BLD574926

Font styles to use
Serif

Colors
00AB8E
00BBA5
67D7C9
C6EFE9
E9F9F6

Requirements
Must have
• logo on the front and details on the back
Nice to have
• sharp and clean lines

```html
<!DOCTYPE html>
<html lang="en">
<head>
<meta charset="utf-8">
<title>RTV CRAFTED — Business Cards</title>
<link href="https://fonts.googleapis.com/css2?family=Tinos:wght@400&display=swap" rel="stylesheet">
<style>
  :root {
    --canvas: #e5e8e7;
    --paper: #ffffff;
    --teal-deep: #00ab8e;
    --teal: #00bba5;
    --teal-soft: #67d7c9;
    --mint: #c6efe9;
    --mint-pale: #e9f9f6;
    --ink: #1f3a36;
    --ink-light: #ffffff;
    --shadow: rgba(0, 0, 0, 0.22);
  }
  * { margin: 0; padding: 0; box-sizing: border-box; }
  html, body {
    width: 1200px; height: 1000px; overflow: hidden;
    background: var(--canvas);
    font-family: "Tinos", "Times New Roman", serif;
  }
  .sheet { position: relative; width: 1200px; height: 1000px; }

  .card {
    position: absolute; width: 482px; height: 290px;
    background: var(--paper);
    box-shadow: 4px 6px 10px var(--shadow);
    overflow: hidden;
  }
  .card--front-light { left: 100px; top: 143px; }
  .card--back-light  { left: 618px; top: 143px; }
  .card--front-dark  { left: 100px; top: 567px; background: var(--teal-deep); }
  .card--back-dark   { left: 618px; top: 567px; }

  /* Front */
  .side-tab { position: absolute; top: 104px; width: 34px; height: 82px; background: var(--teal-deep); }
  .side-tab--left { left: 0; }
  .side-tab--right { right: 0; }
  .card--front-dark .side-tab { background: var(--mint); }

  .wordmark {
    position: absolute; left: 0; right: 0; top: 146px;
    display: flex; align-items: center; justify-content: center; gap: 12px;
  }
  .wordmark__square { width: 18px; height: 18px; background: var(--teal-soft); }
  .card--front-dark .wordmark__square { background: var(--mint); }
  .wordmark__name {
    font-size: 31px; letter-spacing: 0.5px; line-height: 1;
    color: var(--teal-deep);
  }
  .card--front-dark .wordmark__name { color: var(--ink-light); }

  /* Back */
  .services {
    position: absolute; left: 126px; top: 0; width: 229px; height: 185px;
    background: var(--teal-deep); color: var(--ink-light);
    text-align: center;
  }
  .services__title {
    margin-top: 32px; font-size: 17px; font-weight: 400; letter-spacing: 0.3px;
  }
  .services__rule {
    width: 181px; height: 4px; margin: 5px auto 7px; background: var(--mint);
  }
  .services__list { list-style: none; font-size: 12px; line-height: 20.8px; letter-spacing: 0.3px; }

  .contact-bar {
    position: absolute; left: 0; right: 0; top: 218px; height: 72px;
    display: flex; align-items: center;
    font-size: 13.5px; letter-spacing: 0.4px; color: var(--ink);
  }
  .card--back-light .contact-bar { top: 210px; }
  .card--back-dark .contact-bar { background: var(--teal-deep); color: var(--ink-light); top: 218px; }
  .contact { position: absolute; display: flex; align-items: center; gap: 8px; }
  .contact--phone { left: 34px; }
  .contact--email { left: 160px; }
  .contact--licence { left: 350px; gap: 7px; }
  .contact__icon { width: 18px; height: 18px; display: block; }
  .contact__icon-bg { fill: var(--teal); }
  .card--back-dark .contact__icon-bg { fill: var(--teal-soft); }
  .contact__square { width: 18px; height: 18px; background: var(--teal); }
  .card--back-dark .contact__square { background: var(--teal-soft); }
</style>
</head>
<body>
<main class="sheet">

  <section class="card card--front-light" aria-label="Card front, light">
    <div class="side-tab side-tab--left"></div>
    <div class="side-tab side-tab--right"></div>
    <div class="wordmark"><span class="wordmark__square"></span><span class="wordmark__name">RTV CRAFTED</span></div>
  </section>

  <section class="card card--back-light" aria-label="Card back, light">
    <div class="services">
      <h2 class="services__title">BUILDING SERVICES</h2>
      <div class="services__rule"></div>
      <ul class="services__list">
        <li>DECKS</li><li>PERGOLA</li><li>RENOVATION</li><li>EXTENSIONS</li><li>GENERAL BUILDING</li>
      </ul>
    </div>
    <div class="contact-bar">
      <div class="contact contact--phone">
        <svg class="contact__icon" viewBox="0 0 18 18" aria-hidden="true"><rect class="contact__icon-bg" width="18" height="18"/><path d="M4 7.5c0-1.5 2.2-2.5 5-2.5s5 1 5 2.5v1h-2.5v-1.2h-5v1.2H4z M5.5 9.5h7l1 4h-9z" fill="#fff"/></svg>
        <span>0427839152</span>
      </div>
      <div class="contact contact--email">
        <svg class="contact__icon" viewBox="0 0 18 18" aria-hidden="true"><rect class="contact__icon-bg" width="18" height="18"/><path d="M4 4l10 4-4 1.2 3 3-1.3 1.3-3-3L7.5 14z" fill="#fff"/></svg>
        <span>pkharlow47@mailvane.net</span>
      </div>
      <div class="contact contact--licence">
        <span>BLD574926</span><span class="contact__square"></span>
      </div>
    </div>
  </section>

  <section class="card card--front-dark" aria-label="Card front, dark">
    <div class="side-tab side-tab--left"></div>
    <div class="side-tab side-tab--right"></div>
    <div class="wordmark"><span class="wordmark__square"></span><span class="wordmark__name">RTV CRAFTED</span></div>
  </section>

  <section class="card card--back-dark" aria-label="Card back, dark">
    <div class="services">
      <h2 class="services__title">BUILDING SERVICES</h2>
      <div class="services__rule"></div>
      <ul class="services__list">
        <li>DECKS</li><li>PERGOLA</li><li>RENOVATION</li><li>EXTENSIONS</li><li>GENERAL BUILDING</li>
      </ul>
    </div>
    <div class="contact-bar">
      <div class="contact contact--phone">
        <svg class="contact__icon" viewBox="0 0 18 18" aria-hidden="true"><rect class="contact__icon-bg" width="18" height="18"/><path d="M4 7.5c0-1.5 2.2-2.5 5-2.5s5 1 5 2.5v1h-2.5v-1.2h-5v1.2H4z M5.5 9.5h7l1 4h-9z" fill="#fff"/></svg>
        <span>0427839152</span>
      </div>
      <div class="contact contact--email">
        <svg class="contact__icon" viewBox="0 0 18 18" aria-hidden="true"><rect class="contact__icon-bg" width="18" height="18"/><path d="M4 4l10 4-4 1.2 3 3-1.3 1.3-3-3L7.5 14z" fill="#fff"/></svg>
        <span>pkharlow47@mailvane.net</span>
      </div>
      <div class="contact contact--licence">
        <span>BLD574926</span><span class="contact__square"></span>
      </div>
    </div>
  </section>

</main>
</body>
</html>
```